Website design for a Cloud Computing solution company

Name Dorian
Title Head of marketing
Company Name 47Nimbo Solutions Co., Ltd.
E-mail address dorian.feng@47nimbo.example
Present URL (if any) www.47nimbo.example

Description of Project:

The web page style requirements: pages are clean, major color prefer light blue, white and black.
The current 4 Sketches as the page design reference.

What are the top three reasons why you currently have or want to build a Web site?

• Our products are mainly in the online sales.
• Easy to transfer our advantage and features of our product
• Built a communication platform based on cloud computing users to attract more users.

What are the target market that you would like to attract to your Web site and their demographics?

• Small and medium businesses .
• Personal webmaster.
• Startups Company via Internet.

What do you want a person to do once he or she comes to the site?
• Be interested in our product and click on child page to look up more information.
• Contacting with us on-line after browsing

LOOK AND FEEL: List example(s) of sites with a “look and feel” that you would like for your site.

https://www.lumavault.example

SITE ORGANIZATION & LAYOUT: List one or two examples of sites with navigation and layout similar to the one you would like to develop.

https://www.lumavault.example/

FEATURES: Please list all the features/facilities that you would like the website to provide your visitors. To help us understand better, please direct us to a sample site containing the feature.

1) We will use order pages templates and clinent management templates from SERVLEDGR.
2) All ICONs need to be redisigned and prefer to flat design.
3) Prefer to HTML5.
Is there any specific color scheme you want to follow or you like the most?

White and black overall and some light blue.

GRAPHICS: Do you have any graphics/logos/pictures that you would like us to use?

No.

If you have previously had a website, please indicate the features and ingredients that pleased you or displeased you.

No, we don't have existing website.

How can we look at that website?

www.tervanhost.example (Not existing website)

Do you have an existing logo?
No

Industry/Entity Type

Marketing

```html
<!DOCTYPE html>
<html lang="en">
<head>
<meta charset="utf-8">
<title>Tervan Host – Reliability Web Hosting</title>
<link href="https://fonts.googleapis.com/css2?family=Ubuntu:wght@400;500;700&family=Open+Sans:wght@400;600&display=swap" rel="stylesheet">
<style>
:root{
  --teal:#2fc08d;
  --hero-a:#5fbcc8;
  --hero-b:#1a8a9a;
  --ink:#2b2b2b;
  --card:#1f1f1f;
  --card-head:#2a2a2a;
  --muted:#9a9a9a;
  --white:#ffffff;
  --feature-bg-a:#f3f6f8;
  --feature-bg-b:#d9dfe3;
  --footer-a:#4a4a4a;
  --footer-b:#2c2c2c;
  --base:#1b1b1b;
  --blue-btn:#2a8fd0;
  --lime:#8db83a;
}
*{margin:0;padding:0;box-sizing:border-box}
html,body{width:880px;height:1200px;overflow:hidden;background:#fff}
body{position:relative;font-family:"Open Sans",Arial,sans-serif;color:var(--ink)}
.abs{position:absolute}

/* header */
.site-header{position:absolute;left:0;top:0;width:880px;height:66px;background:var(--white)}
.brand{left:126px;top:22px;display:flex;align-items:center;gap:7px;font-family:"Ubuntu",sans-serif;font-weight:500;font-size:18px;color:var(--ink)}
.brand-mark{width:12px;height:12px;border-radius:50%;background:var(--ink)}
.nav-active{left:290px;top:0;width:39px;height:66px;background:var(--teal)}
.nav-link{top:28px;font-size:9.5px;color:#333;white-space:nowrap}
.nav-link.home{color:#fff;left:297px}
.btn-login,.btn-register{top:25px;height:20px;border-radius:2px;font-size:9px;color:#fff;display:flex;align-items:center;justify-content:center}
.btn-login{left:659px;width:43px;background:var(--teal)}
.btn-register{left:709px;width:43px;background:#3a3a3a}

/* hero */
.hero{left:0;top:66px;width:880px;height:384px;background:radial-gradient(ellipse at 45% 35%,var(--hero-a),var(--hero-b) 80%)}
.hero-title{left:130px;top:120px;font-family:"Ubuntu",sans-serif;font-weight:400;font-size:26px;color:#fff;letter-spacing:.3px}
.hero-sub{left:131px;top:157px;font-family:"Ubuntu",sans-serif;font-size:10px;color:#fff}
.hero-point{left:130px;font-family:"Ubuntu",sans-serif;font-size:9.5px;color:#fff;display:flex;align-items:center;gap:7px}
.btn-details{left:130px;top:255px;width:113px;height:30px;background:var(--blue-btn);border-radius:2px;display:flex;align-items:center;color:#fff;font-family:"Ubuntu",sans-serif;font-size:10px}
.btn-details .ico{width:34px;height:30px;background:#1f75b0;display:flex;align-items:center;justify-content:center;margin-right:7px}
.server-art{left:496px;top:62px;width:276px;height:236px;border-radius:30px 30px 10px 10px;background:linear-gradient(160deg,#3a3a3a,#111 60%,#0a0a0a)}
.slider-dots{left:0;top:354px;width:880px;display:flex;justify-content:center;gap:10px}
.slider-dots i{display:block;width:12px;height:12px;border-radius:50%;background:#fff}
.slider-dots i.on{background:#222}

/* promo band */
.promo{left:0;top:450px;width:880px;height:67px;background:var(--teal)}
.promo-text{left:143px;top:24px;font-family:"Ubuntu",sans-serif;font-weight:500;font-size:15px;color:#fff}
.btn-contact{left:626px;top:16px;width:89px;height:35px;background:#2e2e2e;border-radius:2px;color:#fff;font-family:"Ubuntu",sans-serif;font-weight:500;font-size:13px;display:flex;align-items:center;justify-content:center}

/* pricing */
.plan{top:543px;width:181px;height:205px;background:var(--card);border-radius:5px;overflow:hidden;color:#fff;font-family:Arial,Helvetica,sans-serif}
.plan-head{height:32px;background:var(--card-head);border-bottom:1px solid #111;padding-left:20px;font-family:"Ubuntu",sans-serif;font-size:15px;letter-spacing:1.2px;line-height:32px}
.plan-badge{position:absolute;right:8px;top:7px;background:var(--lime);font-size:7px;letter-spacing:0;line-height:15px;padding:0 5px;border-radius:1px;font-weight:700;font-family:Arial,sans-serif}
.plan-price{position:absolute;left:0;top:40px;width:181px;text-align:center;font-size:62px;line-height:70px;font-weight:300}
.plan-price .cur{font-size:22px;vertical-align:top;line-height:40px;margin-right:4px}
.plan-price .per{font-size:6px;margin-left:2px}
.plan-year{position:absolute;top:116px;width:181px;text-align:center;font-size:8.5px}
.plan-bill{position:absolute;top:128px;width:181px;text-align:center;font-size:6.5px;color:var(--muted);letter-spacing:.5px}
.plan-specs{position:absolute;top:140px;left:0;width:181px;border-top:1px solid #3a3a3a;padding:7px 8px;font-size:7.3px;letter-spacing:.8px;line-height:10px}
.plan-specs p+p{margin-top:7px}
.plan-dots{left:0;top:772px;width:880px;display:flex;justify-content:center;gap:9px}
.plan-dots i{display:block;width:12px;height:12px;border-radius:50%;background:#ccc}
.plan-dots i.on{background:var(--teal)}

/* features */
.features{left:0;top:800px;width:880px;height:252px;border-top:1px solid #cfd4d8;background:linear-gradient(var(--feature-bg-a),var(--feature-bg-b))}
.feature{width:210px;height:60px}
.feature-icon{position:absolute;left:-28px;top:-28px;width:56px;height:56px;border-radius:50%;background:#fff;box-shadow:0 1px 4px rgba(0,0,0,.15);display:flex;align-items:center;justify-content:center}
.feature h3{position:absolute;left:35px;top:-18px;font-family:"Ubuntu",sans-serif;font-weight:500;font-size:11.5px;color:#333;white-space:nowrap}
.feature p{position:absolute;left:35px;top:-1px;font-size:9px;color:#444;white-space:nowrap}
.feature a{position:absolute;left:35px;top:14px;font-size:7.5px;color:#333;text-decoration:none;font-weight:600}

/* footer */
.site-footer{left:0;top:1052px;width:880px;height:103px;background:linear-gradient(var(--footer-a),var(--footer-b))}
.footer-rule{left:126px;top:41px;width:486px;height:1px;background:#8a8a8a}
.footer-col{top:24px;color:#fff;font-family:Arial,sans-serif;letter-spacing:.8px}
.footer-col h4{font-weight:400;font-size:10px;margin-bottom:12px}
.footer-col li{list-style:none;font-size:10px;line-height:11.5px}
.social{top:23px;width:20px;height:20px;border-radius:3px;background:linear-gradient(#8ec8ea,#3f8fc6)}
.sales{left:650px;top:58px;color:#fff;font-family:Arial,sans-serif;font-size:11px;letter-spacing:1px}
.base{left:0;top:1155px;width:880px;height:45px;background:var(--base);color:#fff;font-family:Arial,sans-serif;font-size:8px}
.copyright{position:absolute;left:0;top:19px;width:880px;text-align:center}
.version{position:absolute;left:848px;top:19px}
</style>
</head>
<body>

<header class="site-header">
  <div class="abs brand"><span class="brand-mark"></span>Tervan Host</div>
  <div class="abs nav-active"></div>
  <span class="abs nav-link home">Home</span>
  <span class="abs nav-link" style="left:345px">Product</span>
  <span class="abs nav-link" style="left:400px">Control</span>
  <span class="abs nav-link" style="left:453px">Who's on Tervan</span>
  <span class="abs nav-link" style="left:565px">Help</span>
  <span class="abs nav-link" style="left:607px">Company</span>
  <div class="abs btn-login">Login</div>
  <div class="abs btn-register">Register</div>
</header>

<section class="abs hero">
  <svg class="abs" style="left:70px;top:168px" width="22" height="68" viewBox="0 0 22 68"><polyline points="20,2 2,34 20,66" fill="none" stroke="#fff" stroke-width="1.5"/></svg>
  <svg class="abs" style="left:784px;top:168px" width="22" height="68" viewBox="0 0 22 68"><polyline points="2,2 20,34 2,66" fill="none" stroke="#fff" stroke-width="1.5"/></svg>
  <h1 class="abs hero-title">RELIABILITY WEB HOSTING</h1>
  <p class="abs hero-sub">GET YOUR DOMAINS AND FLEXIBLE HOSTING FOR YOUR WEBSITE</p>
  <p class="abs hero-point" style="top:193px">
    <svg width="11" height="11" viewBox="0 0 12 12"><circle cx="6" cy="6" r="6" fill="#fff"/><polyline points="3,6 5.2,8.2 9,4" fill="none" stroke="#1d8fa0" stroke-width="1.6"/></svg>
    UNLIMITED BANDWIDTH WITH MASSIVE STORAGE</p>
  <p class="abs hero-point" style="top:229px">
    <svg width="11" height="11" viewBox="0 0 12 12"><circle cx="6" cy="6" r="6" fill="#fff"/><polyline points="3,6 5.2,8.2 9,4" fill="none" stroke="#1d8fa0" stroke-width="1.6"/></svg>
    UNLIMITED DATABASES AND EMAIL ADDRESSES</p>
  <div class="abs btn-details">
    <span class="ico"><svg width="18" height="18" viewBox="0 0 18 18"><circle cx="9" cy="9" r="7.5" fill="none" stroke="#fff" stroke-width="1.4"/><polyline points="7.5,5.5 11,9 7.5,12.5" fill="none" stroke="#fff" stroke-width="1.6"/></svg></span>
    VIEW DETAILS
  </div>
  <div class="abs server-art" role="img" aria-label="Two glossy black server towers with green light panels"></div>
  <div class="abs slider-dots"><i></i><i class="on"></i><i></i><i></i><i></i></div>
</section>

<section class="abs promo">
  <p class="abs promo-text">Cloud computing is the simple and cheaper way to run your business</p>
  <div class="abs btn-contact">Contact us</div>
</section>

<article class="abs plan" style="left:143px">
  <div class="plan-head">Standard</div>
  <div class="plan-price"><span class="cur">$</span>12<span class="per">/MO</span></div>
  <div class="plan-year">250 $/per year</div>
  <div class="plan-bill">$144.00 billed upon purchase</div>
  <div class="plan-specs"><p>2.4 GHZ&nbsp; 1 CPU+512M Memory<br>50G System Disk+@G Data Disk</p><p>1 Pubilc IP + 1M BGP (NO traffic limited)<br>Multi os templates</p></div>
</article>
<article class="abs plan" style="left:349px">
  <div class="plan-head">Advanced<span class="plan-badge">Most Popular</span></div>
  <div class="plan-price"><span class="cur">$</span>20<span class="per">/MO</span></div>
  <div class="plan-year">350 $/per year</div>
  <div class="plan-bill">$240.00 billed upon purchase</div>
  <div class="plan-specs"><p>2.4 GHZ&nbsp; 1 CPU+512M Memory<br>50G System Disk+@G Data Disk</p><p>1 Pubilc IP + 1M BGP (NO traffic limited)<br>Multi os templates</p></div>
</article>
<article class="abs plan" style="left:554px">
  <div class="plan-head">Luxurious</div>
  <div class="plan-price"><span class="cur">$</span>36<span class="per">/MO</span></div>
  <div class="plan-year">450 $/per year</div>
  <div class="plan-bill">$432.00 billed upon purchase</div>
  <div class="plan-specs"><p>2.4 GHZ&nbsp; 1 CPU+512M Memory<br>50G System Disk+@G Data Disk</p><p>1 Pubilc IP + 1M BGP (NO traffic limited)<br>Multi os templates</p></div>
</article>
<div class="abs plan-dots"><i class="on"></i><i></i><i></i><i></i><i></i></div>

<section class="abs features">
  <div class="abs feature" style="left:154px;top:66px">
    <div class="feature-icon"><svg width="28" height="30" viewBox="0 0 28 30"><path d="M14 2 L25 6 V15 C25 22 19 26 14 28 C9 26 3 22 3 15 V6 Z" fill="none" stroke="var(--teal)" stroke-width="2.5"/><polyline points="9,15 13,19 20,10" fill="none" stroke="var(--teal)" stroke-width="2.5"/></svg></div>
    <h3>STRINGENT SECURITY</h3><p>Dipisicing elit sed do eiusmod</p><a>READ MORE</a>
  </div>
  <div class="abs feature" style="left:369px;top:66px">
    <div class="feature-icon"><svg width="28" height="26" viewBox="0 0 28 26"><rect x="0" y="0" width="28" height="4.5" fill="var(--teal)"/><rect x="0" y="7" width="28" height="4.5" fill="var(--teal)"/><rect x="0" y="14" width="28" height="4.5" fill="var(--teal)"/><rect x="0" y="21" width="28" height="4.5" fill="var(--teal)"/></svg></div>
    <h3>DISTRIBUTED STORE</h3><p>Dipisicing elit sed do eiusmod</p><a>READ MORE</a>
  </div>
  <div class="abs feature" style="left:583px;top:66px">
    <div class="feature-icon"><svg width="34" height="26" viewBox="0 0 34 26"><rect x="1.5" y="1.5" width="31" height="23" fill="none" stroke="var(--teal)" stroke-width="2.5"/><polyline points="7,18 13,11 18,15 27,7" fill="none" stroke="var(--teal)" stroke-width="2.2"/></svg></div>
    <h3>EXCEPTION RELIALIBILITY</h3><p>Dipisicing elit sed do eiusmod</p><a>READ MORE</a>
  </div>
  <div class="abs feature" style="left:154px;top:190px">
    <div class="feature-icon"><svg width="32" height="32" viewBox="0 0 32 32"><circle cx="16" cy="16" r="14" fill="var(--teal)"/><path d="M5 12 C10 10 14 16 20 12 M9 26 C12 20 20 22 24 16" fill="none" stroke="#fff" stroke-width="2.5"/></svg></div>
    <h3>HIGH QUALITY NETWORK</h3><p>Dipisicing elit sed do eiusmod</p><a>READ MORE</a>
  </div>
  <div class="abs feature" style="left:369px;top:190px">
    <div class="feature-icon"><svg width="32" height="32" viewBox="0 0 32 32"><path d="M6 10 A12 12 0 1 1 4 17" fill="none" stroke="var(--teal)" stroke-width="3"/><polyline points="2,6 6,11 11,8" fill="none" stroke="var(--teal)" stroke-width="2.5"/><polyline points="16,9 16,17 21,20" fill="none" stroke="var(--teal)" stroke-width="2.8"/></svg></div>
    <h3>SHORT TIME TO SETUP</h3><p>Dipisicing elit sed do eiusmod</p><a>READ MORE</a>
  </div>
  <div class="abs feature" style="left:583px;top:190px">
    <div class="feature-icon"><svg width="34" height="32" viewBox="0 0 34 32"><path d="M10 5 A13 13 0 1 1 8 26" fill="none" stroke="var(--teal)" stroke-width="2.6"/><path d="M3 10 L7 8 L10 13 L8 15 C9 18 11 20 14 21 L16 19 L21 22 L19 26 C11 26 3 18 3 10 Z" fill="var(--teal)"/><text x="20" y="18" font-family="Arial" font-weight="700" font-size="9" fill="var(--teal)" text-anchor="middle">24</text></svg></div>
    <h3>7*24 MONTIORING</h3><p>Dipisicing elit sed do eiusmod</p><a>READ MORE</a>
  </div>
</section>

<footer class="abs site-footer">
  <div class="abs footer-rule"></div>
  <div class="abs footer-col" style="left:134px"><h4>HELP</h4><ul><li>Guide line</li><li>FAQ</li><li>ICP</li></ul></div>
  <div class="abs footer-col" style="left:278px"><h4>COMPANY</h4><ul><li>About US</li><li>News</li><li>Join us</li></ul></div>
  <div class="abs footer-col" style="left:400px"><h4>CUSTOMERS</h4><ul><li>Game</li><li>Finance</li><li>Others</li></ul></div>
  <div class="abs footer-col" style="left:532px"><h4>SUPPORT</h4><ul><li>Contact Us</li><li>On-line Service</li></ul></div>
  <div class="abs social" style="left:652px"></div>
  <div class="abs social" style="left:678px"></div>
  <div class="abs social" style="left:704px"></div>
  <p class="abs sales">Salse 400-xxx-xxxx</p>
</footer>
<div class="abs base">
  <p class="copyright">Copyright © 2014. All rights reserved.</p>
  <span class="version">C6</span>
</div>

</body>
</html>
```